Professional Lawn Treatment flyer (double sided) needed for established gardening company

We are an established and trusted gardening company in Swindon, UK, and are about to launch a new Lawn Treatment Service. This will be marketed to both existing and new customers and needs to reflect our current professional image. The flyer will need to be double-sided, portrait orientation and correctly sized so to be printed on A5.

If you look on our website www.tavistrowgardening.co.uk, you will see our colours are purple and green. We would like you to use these exact shades of purple and green in your design.

As part of the design, we will need you to put together an infographic table to show our packages. I have attached a spreadsheet which explains these packages but I will need you to create a visually appealing table that fits in with the overall design of the flyer. I don't want you to simply cut and paste my basic table into the design.

In terms of what needs to be included, I have tried to be as specific as possible here but please feel free to message me if you need any further information or clarification.

FRONT SIDE:
The title of our service is:
Expert Lawn Treatment Service

Our strapline will need to be included somewhere:
"Lawn care by your local gardening expert"

The front side of the flyer will need to contain our logo - different versions of which can be found within my dropbox folder here...

https://www.sharebinnu.co.uk/sh/k7qd21mzplax/QRT8xWbnNeLu4Pa-ZxYyhKcLo?dl=0

The front side will need to contain a main image (although feel free to add more if you have anything suitable). I have included a picture in the dropbox folder titled "Front side image" which we would like used. I've also included in the folder an adobe image of grass which you may or may not like to use on either front or back.

Somewhere on both the front and back sides, you will need to include our contact details:
01632 960417
www.tavistrowgardening.co.uk/lawncare

The front side should show what treatments we currently have available. These are:

- Lawn Fertilising
- Scarification
- Aeration
- Weed Control
- Moss Control
- Hydration Booster
- PlumeRest
- Turfing & Renovation

"Select a one-off treatment or choose from one of our specially created lawn care packages."

BACK SIDE:
On the back, we will still need our logo and contact details but the image we'd like used should be the one in the dropbox folder titled "Back side image". Again, if you have any other images you feel would also work, then please feel free to add them.

The back side is to contain a bit more information and be a bit 'wordier' and so can you please include the following 2 paragraphs:

"As expert gardeners, we are passionate about horticulture and working to bring out the very best in your garden. When we work in your garden, we look at it and treat it with the same care and attention as if it were our own, before handing it back for you to enjoy. Our passion doesn't end at just trees and shrubs though. Your grass is as much of a living, breathing plant as your shrubs and we therefore utilise our expert horticultural knowledge to ensure your lawn thrives and reaches its fullest potential.

Lawn care isn't just about applying a fertiliser. It's about really understanding your lawn and being able to use extensive knowledge and experience to diagnose and treat issues. It therefore stands to reason that you should employ an expert to bring out the best in your lawn which is why we at Tavistrow Gardening Services have created a superior lawn care service that will keep your lawn looking lush, green and healthy all year round."

I referred at the very top of this brief to the fact we will need an infographic table created to show the different lawn care packages available. You see from the PDF table I created that we have 3 packages; Standard, Enhanced and Premium. Please create a visually appealing table which sets out the differences between our packages and include it on the back page.

Finally, somewhere we would like reference to the other gardening services we do. It's only to be something small as it isn't the main focus of the flyer but we think it would be good to mention what else we do. To re-iterate, it isnt to be big. I still want the main focus to be lawn care but if you could somehow reference that we also do the following services, that would be good. I will leave it to you to decide where on the flyer it fits in best, be it the front or back:

- Lawn mowing
- Shrub pruning
- Hedge trimming
- Weed killing
- Garden clearance & tidy-up
- Planting & design
- Regular Garden Maintenance
- Turfing
- Fencing
- Gutter clearance

I think thats it. I look forward to your designs!
Ps. Don't forget the dropbox folder:

Target Market(s)

Professional men/women aged 25+
Retired aged 65+

Industry/Entity Type

Home And Garden

Font styles to use
Sans Serif

Colors
6b449b
9bcb3c

Requirements
Must have
• Our company colours; purple and green; as per our website www.tavistrowgardening.co.uk. I've selected purple and green on this brief just to highlight the colours needed but please be sure to use the exact shades from our website and NOT the shade of purple and green that were selected on this brief.
• All the wording as explained in the main project brief.
Nice to have
• I want the flyer to be bold, eye-catching and modern.
• We particularly like the font Trebuchet MS for general copy but please feel free to use any other font for bolder, main titles.
Should not have
• We don't want anything gimmicky. No cheesy marketing.
• We only want professional looking designs. With the greatest of respect, if you're just starting out or don't really do design but think you'll use this as practise, please don't waste your or our time. We've previously run contests for other projects where we've had designs submitted that have clearly been done on MS Word and used Clipart and Wordart. That's really not what we are looking for.

```html
<!DOCTYPE html>
<html lang="en">
<head>
<meta charset="utf-8">
<title>Tavistrow Gardening Services – Lawn Treatment Packages</title>
<link href="https://fonts.googleapis.com/css2?family=Lato:wght@400;700;900&display=swap" rel="stylesheet">
<style>
  :root {
    --purple: #8e2a8b;
    --green: #3db54a;
    --panel: #ececec;
    --ink: #1d1d1d;
    --white: #ffffff;
  }
  * { margin: 0; padding: 0; box-sizing: border-box; }
  html, body { width: 847px; height: 1200px; overflow: hidden; background: #fff; }
  body { font-family: "Lato", sans-serif; color: var(--ink); }
  .flyer { position: relative; width: 847px; height: 1200px; overflow: hidden; }

  .garden-backdrop {
    position: absolute; inset: 0 0 84px 0;
    background:
      radial-gradient(ellipse at 20% 15%, rgba(150,180,140,.35), transparent 55%),
      radial-gradient(ellipse at 75% 85%, rgba(190,195,190,.45), transparent 60%),
      linear-gradient(180deg, #e4ebe0 0%, #f1f3ef 45%, #eceeed 100%);
  }

  .package-tab {
    position: absolute; left: 555px; top: 18px; width: 229px; height: 52px;
    background: var(--green); border-radius: 18px 18px 0 0;
    color: var(--white); font-weight: 900; font-size: 17px; line-height: 18px;
    text-align: center; padding-top: 8px; letter-spacing: .2px;
  }
  .package-panel {
    position: absolute; left: 533px; top: 69px; width: 294px; height: 90px;
    background: var(--panel); border-radius: 22px 0 0 0;
    box-shadow: -2px -2px 6px rgba(0,0,0,.12);
  }
  .package-name {
    position: absolute; top: 88px; width: 90px; text-align: center;
    color: var(--purple); font-weight: 900; font-size: 15.5px; line-height: 17px;
  }

  .treatment-row {
    position: absolute; left: 18px; width: 811px; height: 42px;
    background: var(--purple); border-radius: 21px;
    box-shadow: 0 2px 4px rgba(0,0,0,.18);
    color: var(--white); font-weight: 900; font-size: 18px;
    line-height: 42px; padding-left: 32px;
  }

  .package-grid { position: absolute; left: 0; top: 0; }

  .intro {
    position: absolute; left: 23px; width: 801px;
    font-size: 15.6px; line-height: 25.2px;
    text-align: justify; text-align-last: center;
  }
  .other-services {
    position: absolute; left: 0; top: 908px; width: 847px; text-align: center;
    color: var(--purple); font-weight: 700; font-size: 20.5px; line-height: 29px;
  }
  .service-summary {
    position: absolute; left: 23px; top: 1040px; width: 801px;
    font-size: 15px; line-height: 22px; text-align: justify; text-align-last: center;
  }
  .contact-band {
    position: absolute; left: 0; top: 1116px; width: 847px; height: 84px;
    background: var(--purple); color: var(--white); text-align: center;
    padding-top: 7px;
  }
  .contact-phone { font-size: 26px; letter-spacing: 5px; line-height: 30px; }
  .contact-web { font-size: 26px; letter-spacing: 4.3px; line-height: 30px; }
</style>
</head>
<body>
<main class="flyer">
  <div class="garden-backdrop" role="img" aria-label="Faded photograph of a lawn and garden with a stone path"></div>

  <div class="package-panel"></div>
  <div class="package-tab">LAWN<br>TREATMENT PACKAGES</div>
  <div class="package-name" style="left:535px">Standard<br>Package</div>
  <div class="package-name" style="left:625px">Enhanced<br>Package</div>
  <div class="package-name" style="left:716px">Premium<br>Package</div>

  <div class="treatment-row" style="top:150px">Spring Treatment</div>
  <div class="treatment-row" style="top:200px">Early Summer Treatment</div>
  <div class="treatment-row" style="top:250px">Late Summer Treatment</div>
  <div class="treatment-row" style="top:301px">Autumn/Winter Treatment</div>
  <div class="treatment-row" style="top:352px">Scarification</div>
  <div class="treatment-row" style="top:403px">Aeration</div>
  <div class="treatment-row" style="top:453px">PlumeRest Treatment</div>
  <div class="treatment-row" style="top:504px">Hydration Boost Treatment</div>

  <svg class="package-grid" width="847" height="580" viewBox="0 0 847 580" aria-hidden="true">
    <defs>
      <g id="dot"><circle r="17" fill="var(--green)" stroke="#fff" stroke-width="2.5"/></g>
      <g id="tick">
        <circle r="17" fill="var(--green)" stroke="#fff" stroke-width="2.5"/>
        <circle r="10.5" fill="none" stroke="#fff" stroke-width="2.5"/>
        <path d="M-5 0 L-1.2 4 L5.5 -3.5" fill="none" stroke="#fff" stroke-width="2.8" stroke-linecap="round" stroke-linejoin="round"/>
      </g>
    </defs>
    <g fill="var(--green)" stroke="#fff" stroke-width="2.5">
      <rect x="571" y="136" width="18" height="426" rx="9"/>
      <rect x="661" y="136" width="18" height="426" rx="9"/>
      <rect x="752" y="136" width="18" height="426" rx="9"/>
    </g>
    <g fill="#fff">
      <rect x="578" y="146" width="4" height="406" rx="2"/>
      <rect x="668" y="146" width="4" height="406" rx="2"/>
      <rect x="759" y="146" width="4" height="406" rx="2"/>
    </g>
    <use href="#tick" x="580" y="171"/><use href="#tick" x="670" y="171"/><use href="#tick" x="761" y="171"/>
    <use href="#tick" x="580" y="221"/><use href="#tick" x="670" y="221"/><use href="#tick" x="761" y="221"/>
    <use href="#tick" x="580" y="271"/><use href="#tick" x="670" y="271"/><use href="#tick" x="761" y="271"/>
    <use href="#tick" x="580" y="322"/><use href="#tick" x="670" y="322"/><use href="#tick" x="761" y="322"/>
    <use href="#dot" x="580" y="373"/><use href="#tick" x="670" y="373"/><use href="#tick" x="761" y="373"/>
    <use href="#dot" x="580" y="424"/><use href="#tick" x="670" y="424"/><use href="#tick" x="761" y="424"/>
    <use href="#dot" x="580" y="474"/><use href="#dot" x="670" y="474"/><use href="#tick" x="761" y="474"/>
    <use href="#dot" x="580" y="525"/><use href="#dot" x="670" y="525"/><use href="#tick" x="761" y="525"/>
  </svg>

  <p class="intro" style="top:583px">As expert gardeners, we are passionate about horticulture and working to bring out the very best in your garden. When we work in your garden, we look at it and treat it with the same care and attention as if it were our own, before handing it back for you to enjoy. Our passion doesn't end at just trees and shrubs though. Your grass is as much of a living, breathing plant as your shrubs and we therefore utilise our expert horticultural knowledge to ensure your lawn thrives and reaches its fullest potential.</p>

  <p class="intro" style="top:733px">Lawn care isn't just about applying a fertiliser. It's about really understanding your lawn and being able to use extensive knowledge and experience to diagnose and treat issues. It therefore stands to reason that you should employ an expert to bring out the best in your lawn which is why we at Tavistrow Gardening Services have created a superior lawn care service that will keep your lawn looking lush, green and healthy all year round.</p>

  <p class="other-services">Lawn mowing | Shrub pruning | Hedge trimming | Weed killing<br>Garden clearance &amp; tidy-up | Planting &amp; design | Regular Garden Maintenance<br>Turfing | Fencing | Gutter clearance</p>

  <p class="service-summary">Tavistrow Gardening Services offers a full range of garden maintenance &amp; grounds maintenance services for Swindon. Services include mowing, pruning, hedge trimming, planting &amp; fencing.</p>

  <footer class="contact-band">
    <div class="contact-phone">01632 960417</div>
    <div class="contact-web">www.tavistrowgardening.co.uk/lawncare</div>
  </footer>
</main>
</body>
</html>
```